Automotive component supplier needs a business card design

We need a business card design for our company called Velmar Global Components Ltd based in the UK. We are a supplier of interior and exterior components to premium car manufacturers such as Corvane Hale, Durrant Fyfe, Maxtorn and Valdessimo. We would like to see a modern business card design that uses the colour blue.

Target Market(s)

Premium automotive car manufacturers.

Industry/Entity Type

Automotive

Contact Information for Business Card

Company Name : Velmar Global Components Limited
Address: 17 Tamsey Yard, Upper Drisk, Warwick, CV31 8RJ, United Kingdom
Web Address : www.velmarparts-example.co.uk

Font styles to use
Other font styles liked:
• Helvetica

Colors
3176b5
0255a3
85acd3
cfdeed
cee9f5
85cae6
34a6d7
0692cd
9bcb3c

Requirements
Must have
• Clear company logo and a mixture of blue colours.
Nice to have
• A high quality modern image.
Should not have
• Multiple colours.

```html
<!DOCTYPE html>
<html lang="en">
<head>
<meta charset="utf-8">
<title>Velmar Global Components – Business Card</title>
<link href="https://fonts.googleapis.com/css2?family=Arimo:wght@400;700&display=swap" rel="stylesheet">
<style>
  :root {
    --blue: #0692cd;
    --blue-deep: #0255a3;
    --blue-mid: #3176b5;
    --green: #9bcb3c;
    --paper: #ffffff;
    --backdrop: #e6e9ec;
    --ink-shadow: rgba(20, 30, 40, 0.18);
  }
  * { box-sizing: border-box; margin: 0; padding: 0; }
  html, body {
    width: 1200px; height: 900px; overflow: hidden;
    background: var(--backdrop);
    font-family: "Arimo", Helvetica, Arial, sans-serif;
  }
  .sheet {
    width: 1200px; height: 900px;
    display: flex; flex-direction: column; align-items: center; justify-content: center;
    gap: 44px;
  }
  .card {
    position: relative;
    width: 640px; height: 366px;
    background: var(--paper);
    box-shadow: 0 10px 28px var(--ink-shadow);
    overflow: hidden;
  }
  /* Wordmark */
  .wordmark {
    display: flex; align-items: center; gap: 12px;
    color: var(--blue);
    font-weight: 700;
    text-transform: uppercase;
    letter-spacing: 0.02em;
    line-height: 1.05;
  }
  .wordmark__square {
    width: 16px; height: 16px; background: var(--green); flex: none;
  }
  /* Back */
  .card--back {
    display: flex; flex-direction: column; align-items: center; justify-content: center;
    gap: 34px;
  }
  .card--back .wordmark { font-size: 34px; }
  .card--back .web {
    color: var(--blue);
    font-weight: 700; font-size: 16px; letter-spacing: 0.04em; text-transform: uppercase;
  }
  /* Front */
  .card--front .wordmark {
    position: absolute; left: 34px; top: 118px; width: 250px;
    font-size: 27px;
  }
  .divider {
    position: absolute; left: 306px; top: 96px; width: 1px; height: 160px;
    background: var(--blue);
  }
  .contact {
    position: absolute; left: 328px; top: 104px;
  }
  .contact__name {
    color: var(--blue); font-weight: 700; font-size: 26px; text-transform: uppercase; letter-spacing: 0.02em;
  }
  .contact__role {
    color: var(--green); font-weight: 700; font-size: 15px; text-transform: uppercase; letter-spacing: 0.03em;
    margin: 2px 0 12px;
  }
  .contact__list { list-style: none; }
  .contact__item {
    display: flex; align-items: center; gap: 9px;
    color: var(--blue-deep); font-size: 16px; line-height: 25px;
  }
  .contact__icon { width: 15px; height: 15px; flex: none; }
  .address-band {
    position: absolute; left: 0; right: 0; top: 284px; height: 44px;
    background: var(--blue);
    display: flex; align-items: center; padding-left: 34px;
    color: var(--paper); font-weight: 700; font-size: 16px; letter-spacing: 0.01em;
  }
</style>
</head>
<body>
<main class="sheet">
  <section class="card card--back" aria-label="Business card back">
    <div class="wordmark">
      <span class="wordmark__square"></span>
      <span>Velmar Global Components</span>
    </div>
    <p class="web">www.velmarparts-example.co.uk</p>
  </section>

  <section class="card card--front" aria-label="Business card front">
    <div class="wordmark">
      <span>Velmar Global Components</span>
    </div>
    <div class="divider"></div>
    <div class="contact">
      <h1 class="contact__name">Rowan Petch</h1>
      <p class="contact__role">Managing Director</p>
      <ul class="contact__list">
        <li class="contact__item">
          <svg class="contact__icon" viewBox="0 0 16 16"><rect x="4" y="1" width="8" height="14" rx="1.5" fill="none" stroke="#9bcb3c" stroke-width="1.6"/><circle cx="8" cy="12.5" r="0.9" fill="#9bcb3c"/></svg>
          045 710 286
        </li>
        <li class="contact__item">
          <svg class="contact__icon" viewBox="0 0 16 16"><path d="M3.5 1.5l3 3-1.6 1.8c.9 2 2.4 3.5 4.3 4.3l1.8-1.6 3 3-1.8 2C7 13.6 2.4 9 1.5 3.3z" fill="#9bcb3c"/></svg>
          234 905 817
        </li>
        <li class="contact__item">
          <svg class="contact__icon" viewBox="0 0 16 16"><rect x="1" y="3" width="14" height="10" fill="#9bcb3c"/><path d="M1 3l7 5.5L15 3" fill="none" stroke="#fff" stroke-width="1.3"/></svg>
          hello@velmarparts-example.co.uk
        </li>
        <li class="contact__item">
          <svg class="contact__icon" viewBox="0 0 16 16"><circle cx="8" cy="8" r="6.5" fill="none" stroke="#9bcb3c" stroke-width="1.4"/><ellipse cx="8" cy="8" rx="2.8" ry="6.5" fill="none" stroke="#9bcb3c" stroke-width="1.2"/><path d="M1.5 8h13M2.5 4.8h11M2.5 11.2h11" stroke="#9bcb3c" stroke-width="1.1"/></svg>
          www.velmarparts-example.co.uk
        </li>
      </ul>
    </div>
    <div class="address-band">17 Tamsey Yard, Upper Drisk, Warwick, CV31 8RJ, United Kingdom</div>
  </section>
</main>
</body>
</html>
```